Breakthrough Sports Drink Needs a Label Design

Using the logo provided, we need a label design for a new sports drink company called 'Vorna'. We have developed a clear and light, protein-infused beverage for elite athletes.

We would like to label to use a similar color scheme as the logo provided. It needs to portray a refreshing, healthy feel but also needs to reflect the functional aspects of the drink.

The label needs to clearly include the phrases: "18 grams of protein", "For the Elite Athlete" and " "2:1 ratio of carbs to protein "

Target Market(s)

College Athletes

Industry/Entity Type

It Company

Requirements
Must have
• Should be based on the logo provided and include the phrases:
• 18g of Protein
• For The Elite Athlete
• 2:1 Ratio of Carbs to Protein

```html
<!DOCTYPE html>
<html lang="en">
<head>
<meta charset="utf-8">
<title>Vorna Athletic Recovery Label</title>
<link rel="stylesheet" href="https://fonts.googleapis.com/css2?family=Noto+Sans:wght@700;800;900&display=swap">
<style>
  :root {
    --sky: #c9e2f4;
    --sky-deep: #9fd0ee;
    --facet-grey: #e4e6e8;
    --facet-light: #f1f3f5;
    --ink: #2e3a46;
    --blue: #0b63b0;
    --blue-light: #2f8fd8;
    --green: #7fd13a;
    --green-dark: #1f8a2e;
    --orange: #ff7a00;
    --orange-deep: #ff4a00;
    --white: #ffffff;
  }
  html, body {
    margin: 0;
    padding: 0;
    width: 1200px;
    height: 822px;
    overflow: hidden;
    background: var(--sky);
  }
  .label {
    display: block;
    width: 1200px;
    height: 822px;
    font-family: "Noto Sans", Verdana, sans-serif;
  }
  .brand-name { font-weight: 900; font-size: 186px; fill: var(--ink); letter-spacing: -4px; }
  .brand-tagline { font-weight: 800; font-size: 52px; letter-spacing: 9px; }
  .ribbon-text { font-weight: 800; fill: var(--white); }
  .ratio-value { font-weight: 900; font-size: 58px; fill: var(--white); stroke: #5a2a00; stroke-width: 1.5px; paint-order: stroke; }
  .protein-number { font-weight: 900; font-size: 168px; fill: var(--blue); stroke: var(--white); stroke-width: 3px; paint-order: stroke; letter-spacing: -14px; }
</style>
</head>
<body>
<svg class="label" viewBox="0 0 1200 822" xmlns="http://www.w3.org/2000/svg">
  <defs>
    <linearGradient id="taglineGrad" x1="0" y1="0" x2="0" y2="1">
      <stop offset="0" stop-color="#3aa0e8"/>
      <stop offset="1" stop-color="#0a4f99"/>
    </linearGradient>
    <linearGradient id="greenGrad" x1="0" y1="0" x2="1" y2="0">
      <stop offset="0" stop-color="#5cc028"/>
      <stop offset="0.55" stop-color="#a8f040"/>
      <stop offset="0.7" stop-color="#d6f7b0"/>
      <stop offset="1" stop-color="#4caf2c"/>
    </linearGradient>
    <linearGradient id="orangeGrad" x1="0" y1="0" x2="1" y2="0">
      <stop offset="0" stop-color="#ff4a00"/>
      <stop offset="0.7" stop-color="#ff8c00"/>
      <stop offset="1" stop-color="#c83c00"/>
    </linearGradient>
    <linearGradient id="blueGrad" x1="0" y1="0" x2="1" y2="0">
      <stop offset="0" stop-color="#0b5fa8"/>
      <stop offset="0.4" stop-color="#7fb6e2"/>
      <stop offset="1" stop-color="#0b63b0"/>
    </linearGradient>
  </defs>

  <!-- background facets -->
  <g class="background">
    <rect width="1200" height="822" fill="var(--sky)"/>
    <polygon points="200,0 1000,0 700,822 260,822" fill="var(--facet-grey)"/>
    <polygon points="380,0 1200,0 1200,160 280,480" fill="var(--facet-light)" opacity="0.8"/>
    <polygon points="0,300 280,480 0,560" fill="var(--facet-grey)"/>
    <polygon points="1030,220 1200,300 1200,822 980,822" fill="var(--sky-deep)" opacity="0.6"/>
    <polygon points="700,560 1200,300 1200,540" fill="var(--sky)" opacity="0.7"/>
    <polygon points="0,560 280,480 360,822 0,822" fill="var(--sky)"/>
  </g>

  <!-- brand -->
  <g class="brand">
    <text class="brand-name" x="600" y="210" text-anchor="middle">VORNA</text>
    <text class="brand-tagline" x="596" y="287" text-anchor="middle" fill="url(#taglineGrad)">ATHLETIC RECOVERY</text>
  </g>

  <!-- faint decorations -->
  <rect class="heart-mark" role="img" aria-label="Faint green heart outline" x="384" y="296" width="128" height="88" rx="30" fill="#d6ecd0" opacity="0.5"/>
  <rect class="runner-mark" role="img" aria-label="Faint blue running figure" x="384" y="432" width="96" height="88" rx="20" fill="#a9c8de" opacity="0.55"/>

  <!-- elite athlete ribbon -->
  <g class="ribbon-elite">
    <polygon points="500,650 575,610 505,706" fill="var(--green-dark)"/>
    <polygon points="130,476 590,564 575,650 120,584" fill="url(#greenGrad)"/>
    <rect class="athlete-figure" role="img" aria-label="Green running athlete silhouette" x="74" y="458" width="56" height="120" rx="14" fill="var(--green)"/>
    <text class="ribbon-text" x="132" y="538" font-size="40" transform="rotate(10.5 132 538)">For the Elite Athlete</text>
  </g>

  <!-- ratio ribbon -->
  <g class="ribbon-ratio">
    <polygon points="640,500 740,480 690,530" fill="#b84a00"/>
    <polygon points="620,400 1064,302 1040,420 640,500" fill="url(#orangeGrad)"/>
    <polygon points="1064,302 1105,380 1040,420" fill="var(--orange)"/>
    <text class="ribbon-text" x="694" y="424" font-size="37" transform="rotate(-12 694 424)">Ratio of Carbs</text>
    <text class="ribbon-text" x="740" y="460" font-size="37" transform="rotate(-12 740 460)">to Protein</text>
    <circle cx="1032" cy="476" r="76" fill="var(--white)"/>
    <circle cx="1032" cy="476" r="62" fill="var(--orange)"/>
    <text class="ratio-value" x="1032" y="497" text-anchor="middle">2:1</text>
  </g>

  <!-- protein banner -->
  <g class="banner-protein">
    <rect x="740" y="664" width="460" height="116" fill="url(#blueGrad)"/>
    <rect x="650" y="646" width="120" height="112" fill="var(--blue)"/>
    <text class="protein-number" x="618" y="755">18</text>
    <text class="ribbon-text" x="804" y="735" font-size="40">grams of Protein</text>
  </g>
</svg>
</body>
</html>
```